Women's Health Company needs business card

We need a business card for a USA based women's health care company. We use digital technology to enhance therapy prescribed by clinicians for their patients

```html
<!DOCTYPE html>
<html lang="en">
<head>
<meta charset="utf-8">
<title>Lumira Health – Business Card</title>
<link rel="stylesheet" href="https://fonts.googleapis.com/css2?family=Roboto:wght@400;700&display=swap">
<style>
  :root{
    --purple:#8e55a0;
    --teal:#6fbfba;
    --white:#ffffff;
    --stage:#c9c9c9;
    --stage-dark:#a9a9a9;
  }
  *{margin:0;padding:0;box-sizing:border-box}
  html,body{width:1200px;height:788px;overflow:hidden}
  body{
    background:linear-gradient(180deg,var(--stage) 0%,var(--stage-dark) 100%);
    font-family:'Roboto',Arial,sans-serif;
    position:relative;
  }
  .card{
    position:absolute;
    width:540px;height:308px;
    border-radius:22px;
    overflow:hidden;
    box-shadow:0 10px 28px rgba(0,0,0,.22);
  }
  .card--front{left:40px;top:240px;background:var(--white)}
  .card--back{left:620px;top:240px;background:var(--purple)}
  .card__art{position:absolute;inset:0;width:100%;height:100%}

  .brand-name{
    font-family:'Roboto',Arial,sans-serif;
    font-weight:400;
    color:var(--teal);
    white-space:nowrap;
  }
  .card--front .brand-name{
    position:absolute;left:30px;top:118px;font-size:34px;
  }
  .card--back .brand-name{
    position:absolute;left:0;right:0;top:122px;text-align:center;font-size:54px;
  }

  .contact{
    position:absolute;right:26px;top:34px;
    text-align:right;color:var(--white);
  }
  .contact__name{
    font-weight:700;font-size:19px;letter-spacing:.5px;color:var(--teal);
    text-transform:uppercase;
  }
  .contact__role{font-size:13px;margin-bottom:16px}
  .contact__list{list-style:none}
  .contact__item{
    font-size:13px;line-height:20px;
    display:flex;justify-content:flex-end;align-items:center;gap:7px;
  }
  .contact__icon{width:11px;height:11px;flex:none}
</style>
</head>
<body>

<section class="card card--front" aria-label="Business card front">
  <svg class="card__art" viewBox="0 0 540 308" aria-hidden="true">
    <path d="M430 0 L540 0 L540 308 L90 308 C180 300 222 250 252 170 C292 62 342 10 430 0 Z" fill="var(--purple)"/>
    <path d="M420 0 C334 12 284 62 244 168 C214 248 170 298 78 308" fill="none" stroke="var(--teal)" stroke-width="6"/>
  </svg>

  <div class="brand-name">Lumira Health</div>

  <div class="contact">
    <p class="contact__name">Daniel Reyes</p>
    <p class="contact__role">CEO/Founder</p>
    <ul class="contact__list">
      <li class="contact__item">(555) 218-4630
        <svg class="contact__icon" viewBox="0 0 12 12"><path d="M2.5 1 L4.5 1 L5.2 3.6 L3.9 4.6 C4.6 6 6 7.4 7.4 8.1 L8.4 6.8 L11 7.5 L11 9.5 C11 10.3 10.3 11 9.5 11 C5 11 1 7 1 2.5 C1 1.7 1.7 1 2.5 1 Z" fill="var(--white)"/></svg>
      </li>
      <li class="contact__item">(555) 371-9024
        <svg class="contact__icon" viewBox="0 0 12 12"><rect x="3" y="0.8" width="6" height="10.4" rx="1.2" fill="none" stroke="var(--white)" stroke-width="1.2"/><circle cx="6" cy="9.4" r=".7" fill="var(--white)"/></svg>
      </li>
      <li class="contact__item">hello@lumirahealth.com
        <svg class="contact__icon" viewBox="0 0 12 12"><rect x="0.8" y="2.3" width="10.4" height="7.4" fill="var(--white)"/><path d="M1 2.6 L6 6.4 L11 2.6" fill="none" stroke="var(--purple)" stroke-width="1"/></svg>
      </li>
      <li class="contact__item">www.lumirahealth.com
        <svg class="contact__icon" viewBox="0 0 12 12"><circle cx="6" cy="6" r="5" fill="none" stroke="var(--white)" stroke-width="1.1"/><ellipse cx="6" cy="6" rx="2.2" ry="5" fill="none" stroke="var(--white)" stroke-width="1"/><path d="M1 6 H11" stroke="var(--white)" stroke-width="1"/></svg>
      </li>
    </ul>
  </div>
</section>

<section class="card card--back" aria-label="Business card back">
  <div class="brand-name">Lumira Health</div>
</section>

</body>
</html>
```